Modern Business Card for Industrial Company

We need business cards updated with modern fonts and make it look more technical, sharp and clean. The logo should not be changed, but we are looking for fresh solutions for how other information on the card is laid out in an interesting way. The company provides machinery and services to the ceramic industry and deals with cutting-edge technology. The design should reflect a technologically advanced and modern company that deals with the latest European technologies.

Font styles to use
Sans Serif

Requirements
Must have
• Modern fonts, technical look and feel

```html
<!DOCTYPE html>
<html lang="en">
<head>
<meta charset="utf-8">
<title>KR Tecno – Business Card</title>
<link href="https://fonts.googleapis.com/css2?family=Michroma&display=swap" rel="stylesheet">
<style>
  :root {
    --bg: #1d1d1e;
    --card: #161617;
    --card-edge: #0c0c0d;
    --blue: #1f6dc2;
    --blue-soft: rgba(31, 109, 194, 0.55);
    --red: #d23232;
    --white: #f2f2f2;
    --grey: #bfc2c6;
    --muted: #3a3a3c;
  }
  * { box-sizing: border-box; margin: 0; padding: 0; }
  html, body { width: 1200px; height: 1200px; overflow: hidden; }
  body {
    background: radial-gradient(circle at 50% 35%, #262627 0%, var(--bg) 70%);
    font-family: "Michroma", sans-serif;
    color: var(--white);
    position: relative;
  }
  .card {
    position: absolute;
    left: 180px;
    width: 840px;
    height: 480px;
    background: var(--card);
    box-shadow: 0 18px 40px rgba(0,0,0,0.6);
    overflow: hidden;
  }
  .card--back { top: 70px; }
  .card--front { top: 610px; }

  /* back */
  .back-brand {
    position: absolute; top: 170px; left: 0; width: 100%;
    text-align: center; font-size: 64px; letter-spacing: 4px; color: var(--grey);
  }
  .back-web {
    position: absolute; bottom: 56px; left: 0; width: 100%;
    text-align: center; font-size: 17px; letter-spacing: 2px; color: #6a6c70;
  }

  /* front */
  .pattern {
    position: absolute;
    background: radial-gradient(ellipse at center, var(--blue-soft) 0%, rgba(31,109,194,0.15) 55%, transparent 75%);
  }
  .pattern--tl { top: -30px; left: -10px; width: 260px; height: 110px; }
  .pattern--tr { top: 80px; right: -20px; width: 380px; height: 110px; }
  .pattern--ml { top: 260px; left: -60px; width: 140px; height: 190px; }
  .pattern--br { bottom: -30px; right: -10px; width: 380px; height: 120px; }

  .brand {
    position: absolute; top: 70px; left: 60px;
    font-size: 58px; letter-spacing: 3px; color: var(--blue); line-height: 1.2;
  }
  .person { position: absolute; top: 150px; right: 70px; text-align: right; }
  .person__name { font-size: 23px; letter-spacing: 2px; color: var(--white); }
  .person__title { font-size: 20px; letter-spacing: 2px; color: var(--red); margin-top: 6px; }

  .rule { position: absolute; height: 3px; }
  .rule--red { top: 300px; left: 60px; width: 400px; background: var(--red); }
  .rule--blue { top: 318px; left: 475px; width: 305px; background: var(--blue); }

  .contacts { position: absolute; top: 330px; left: 60px; list-style: none; }
  .contacts li {
    display: flex; align-items: center; gap: 14px;
    font-size: 17px; letter-spacing: 1px; height: 34px;
  }
  .icon {
    width: 24px; height: 24px; background: var(--red); border-radius: 3px;
    display: flex; align-items: center; justify-content: center; flex: none;
  }
  .icon svg { width: 16px; height: 16px; }

  .address {
    position: absolute; top: 342px; right: 60px;
    display: flex; align-items: center; gap: 14px;
  }
  .address__text { text-align: right; font-size: 17px; letter-spacing: 1px; line-height: 34px; }
</style>
</head>
<body>

<section class="card card--back">
  <div class="back-brand">KR TECNO</div>
  <div class="back-web">WWW.KRTECNO.COM</div>
</section>

<section class="card card--front">
  <div class="pattern pattern--tl" role="img" aria-label="Blue pixel-grid decoration"></div>
  <div class="pattern pattern--tr" role="img" aria-label="Blue pixel-grid decoration"></div>
  <div class="pattern pattern--ml" role="img" aria-label="Blue pixel-grid decoration"></div>
  <div class="pattern pattern--br" role="img" aria-label="Blue pixel-grid decoration"></div>

  <div class="brand">KR TECNO</div>

  <div class="person">
    <div class="person__name">MARCO DELLARI</div>
    <div class="person__title">PRESIDENT</div>
  </div>

  <div class="rule rule--red"></div>
  <div class="rule rule--blue"></div>

  <ul class="contacts">
    <li>
      <span class="icon"><svg viewBox="0 0 16 16"><path fill="#fff" d="M4 1.5l2 3-1.3 1.3a8 8 0 0 0 5.5 5.5L11.5 10l3 2-.8 2.2C12.9 15 5 14 2 6.2 1.3 4.7 1.5 2.8 4 1.5z"/></svg></span>
      404-555-0172
    </li>
    <li>
      <span class="icon"><svg viewBox="0 0 16 16"><rect x="1.5" y="3.5" width="13" height="9" fill="none" stroke="#fff" stroke-width="1.4"/><path d="M1.5 3.5L8 9l6.5-5.5" fill="none" stroke="#fff" stroke-width="1.4"/></svg></span>
      MDELLARI@KRTECNO.COM
    </li>
    <li>
      <span class="icon"><svg viewBox="0 0 16 16" fill="none" stroke="#fff" stroke-width="1.2"><circle cx="8" cy="8" r="6.2"/><ellipse cx="8" cy="8" rx="2.7" ry="6.2"/><path d="M1.8 8h12.4M2.8 5h10.4M2.8 11h10.4"/></svg></span>
      WWW.KRTECNO.COM
    </li>
  </ul>

  <div class="address">
    <div class="address__text">418 MERIDIAN WAY, SUITE 200<br>DUNMORE, GA 30412</div>
    <span class="icon"><svg viewBox="0 0 16 16"><path fill="#fff" d="M8 1a5 5 0 0 0-5 5c0 3.6 5 9 5 9s5-5.4 5-9a5 5 0 0 0-5-5zm0 7a2 2 0 1 1 0-4 2 2 0 0 1 0 4z"/></svg></span>
  </div>
</section>

</body>
</html>
```